Business cards for KORBEN Real Estate Properties LLC

We need a cool, original business card design for a company based in the Washington DC metropolitan area. We are a new energetic and passionate Real Estate Investing Company that invests in all types of real estate; commercial, residential, industrial etc.

Our company color is Red since it reflects action, energy and speed; it is assertive confident, energizing, exciting, powerful, passionate and determined. So we would like business card communicate those qualities to the audience.

Our audiences are investors that want to invest with us, real estate sellers, buyers, and tenants who lease from us.

Our logo is attached

```html
<!DOCTYPE html>
<html lang="en">
<head>
<meta charset="utf-8">
<title>KORBEN Real Estate Properties LLC — Business Cards</title>
<link href="https://fonts.googleapis.com/css2?family=Quicksand:wght@400;500;700&display=swap" rel="stylesheet">
<style>
  :root {
    --stage: #1c1c1c;
    --brand-red: #ff0000;
    --band-grey: #e4e4e4;
    --ink: #111111;
    --paper: #ffffff;
    --ghost: rgba(0, 0, 0, 0.06);
  }
  * { box-sizing: border-box; margin: 0; padding: 0; }
  html, body { width: 1200px; height: 1000px; overflow: hidden; }
  body {
    background: var(--stage);
    font-family: "Quicksand", sans-serif;
    position: relative;
  }
  .card {
    position: absolute;
    width: 640px;
    height: 366px;
    background: var(--brand-red);
    border-radius: 8px;
    overflow: hidden;
    box-shadow: 0 10px 30px rgba(0, 0, 0, 0.5);
  }
  .card--front { left: 280px; top: 80px; }
  .card--back { left: 280px; top: 540px; }

  /* Front */
  .front-name {
    position: absolute;
    left: 0; right: 0; top: 110px;
    text-align: center;
    color: var(--ink);
    font-weight: 700;
  }
  .front-name .word { display: block; font-size: 76px; letter-spacing: 4px; line-height: 1; }
  .front-name .sub { display: block; font-size: 22px; letter-spacing: 1px; margin-top: 8px; }
  .front-web {
    position: absolute;
    left: 0; right: 0; top: 290px;
    display: flex; justify-content: center; align-items: center; gap: 10px;
    color: var(--paper);
    font-size: 17px;
  }

  /* Back */
  .band {
    position: absolute;
    left: 0; right: 0; top: 78px; height: 170px;
    background: var(--band-grey);
  }
  .band-ghost {
    position: absolute;
    left: 190px; top: 40px;
    font-size: 110px; font-weight: 700; letter-spacing: 6px;
    color: var(--ghost);
    line-height: 1;
  }
  .holder {
    position: absolute;
    left: 40px; top: 20px;
    color: var(--ink);
  }
  .holder .word { font-size: 26px; font-weight: 700; letter-spacing: 1px; }
  .holder .sub { font-size: 15px; font-weight: 500; margin-top: 2px; }
  .band-mark {
    position: absolute;
    right: 40px; top: 58px;
    color: var(--ink); font-weight: 700; text-align: right;
  }
  .band-mark .word { font-size: 36px; letter-spacing: 2px; line-height: 1; }
  .band-mark .sub { font-size: 10px; margin-top: 4px; }
  .contact {
    position: absolute;
    left: 40px; top: 110px;
    list-style: none;
    color: var(--paper);
    font-size: 16px;
    z-index: 2;
  }
  .contact li { display: flex; align-items: center; gap: 10px; margin-bottom: 8px; }
  .contact svg { flex: none; }
</style>
</head>
<body>

<section class="card card--front" aria-label="Business card front">
  <div class="front-name">
    <span class="word">KORBEN</span>
    <span class="sub">REAL ESTATE PROPERTIES LLC</span>
  </div>
  <div class="front-web">
    <svg width="16" height="16" viewBox="0 0 16 16" aria-hidden="true">
      <circle cx="8" cy="8" r="7" fill="none" stroke="#fff" stroke-width="1.5"/>
      <path d="M1 8h14M8 1c3 3 3 11 0 14M8 1c-3 3-3 11 0 14" fill="none" stroke="#fff" stroke-width="1.2"/>
    </svg>
    <span>www.korbenproperties.com</span>
  </div>
</section>

<section class="card card--back" aria-label="Business card back">
  <div class="band">
    <div class="band-ghost" aria-hidden="true">KORBEN</div>
    <div class="holder">
      <div class="word">KORBEN</div>
      <div class="sub">Real Estate Properties LLC</div>
    </div>
    <div class="band-mark">
      <div class="word">KORBEN</div>
      <div class="sub">REAL ESTATE PROPERTIES LLC</div>
    </div>
    <ul class="contact">
      <li>
        <svg width="14" height="14" viewBox="0 0 16 16" aria-hidden="true">
          <path d="M4 1l3 3-2 2c1 2 3 4 5 5l2-2 3 3-2 2C7 14 2 9 2 3z" fill="#111"/>
        </svg>
        <span style="color:#111">000000000</span>
      </li>
    </ul>
  </div>
  <ul class="contact" style="top: 262px;">
    <li>
      <svg width="14" height="14" viewBox="0 0 16 16" aria-hidden="true">
        <circle cx="8" cy="8" r="7" fill="none" stroke="#fff" stroke-width="1.5"/>
        <path d="M1 8h14M8 1c3 3 3 11 0 14M8 1c-3 3-3 11 0 14" fill="none" stroke="#fff" stroke-width="1.2"/>
      </svg>
      <span>www.korbenproperties.com</span>
    </li>
  </ul>
</section>

</body>
</html>
```